Design for product lable
MERO LUX
COMMING SOON
background design for nutrition products
such as whey protein powders Cretin and so on
this well be our background style
all the fallowing products gonna look nearly the same so the wining design well work on all other products we produce background our bottle color is black we have blue and gold on our logo
athlete, mostly fitness and bodybuilders
and all others sports
it must come in 4 flavor variants : chocolate, vanilla, strawberry,banana
pleas avoid using to many braid colors
try to give a royal look to it thank you
remember it is 250 because separately for each product if you are a wining project then we make a deal what we gonna pay for the each fallowing product
amino profile total hight 6cm
weight 12 cm
color wight or must much whit the label color or whit background blact text
this is a bad resolution so pleas make new charts

```html
<!DOCTYPE html>
<html lang="en">
<head>
<meta charset="utf-8">
<title>MERO LUX – Protein Label Variants</title>
<link rel="stylesheet" href="https://fonts.googleapis.com/css2?family=Oswald:wght@500;700&family=Roboto+Condensed:wght@400;700&display=swap">
<style>
  :root {
    --page: #0d0d0f;
    --ink: #ffffff;
    --ink-soft: rgba(255,255,255,0.72);
    --band: #070708;
    --accent-blue: #3f7fd6;
    --accent-gold: #d9a63a;
    --chocolate: #4a2414;
    --banana: #6b5a12;
    --strawberry: #6e0d14;
    --vanilla: #0f2a63;
  }
  * { box-sizing: border-box; margin: 0; padding: 0; }
  html, body { width: 1200px; height: 901px; overflow: hidden; background: var(--page); }
  body { font-family: "Roboto Condensed", Arial, sans-serif; color: var(--ink); }
  .sheet { padding: 30px 20px 0; display: flex; flex-direction: column; gap: 17px; }

  .label {
    position: relative; height: 200px; border-radius: 4px; overflow: hidden;
    background:
      radial-gradient(ellipse at 30% 55%, rgba(255,255,255,0.14), transparent 60%),
      linear-gradient(180deg, var(--tone) 0%, #000 130%);
  }
  .label--chocolate { --tone: var(--chocolate); }
  .label--banana { --tone: var(--banana); }
  .label--strawberry { --tone: var(--strawberry); }
  .label--vanilla { --tone: var(--vanilla); }

  .band { position: absolute; left: 0; right: 0; height: 18px; background: var(--band); }
  .band--top { top: 0; border-bottom: 1px solid rgba(255,255,255,0.25); }
  .band--bottom { bottom: 0; border-top: 1px solid rgba(255,255,255,0.25); }
  .flavor { position: absolute; top: 3px; left: 18px; font-size: 11px; color: var(--ink-soft); }

  .front { position: absolute; left: 24px; top: 24px; width: 640px; }
  .brand { display: flex; align-items: center; gap: 8px; }
  .brand-dot { width: 14px; height: 14px; border-radius: 50%; background: var(--accent-blue); }
  .brand-name { font-family: "Oswald", sans-serif; font-weight: 500; font-size: 20px; letter-spacing: 1px; }
  .brand-tagline { font-size: 9px; letter-spacing: 3px; color: var(--ink-soft); margin-left: 22px; }
  .product-name {
    font-family: "Oswald", sans-serif; font-weight: 700; font-size: 72px; line-height: 1;
    letter-spacing: 1px; margin-top: 2px;
  }
  .ingredients { font-size: 13px; font-weight: 700; letter-spacing: 0.5px; margin-top: 4px; }
  .net-weight { position: absolute; bottom: 2px; left: 24px; font-size: 11px; color: var(--ink-soft); }

  .badges { position: absolute; left: 470px; bottom: 30px; display: flex; gap: 10px; }
  .badge { width: 22px; height: 22px; border-radius: 3px; background: rgba(255,255,255,0.22); }

  .side {
    position: absolute; right: 24px; top: 30px; width: 400px;
    border-left: 1px solid rgba(255,255,255,0.18); padding-left: 20px;
  }
  .side-title { font-family: "Oswald", sans-serif; font-weight: 700; font-size: 24px; }
  .side-copy { font-size: 11px; line-height: 1.45; color: var(--ink-soft); margin-top: 6px; }
  .side-brand { display: flex; align-items: center; gap: 6px; margin-top: 14px; justify-content: flex-end; }
  .side-brand .brand-dot { width: 10px; height: 10px; background: var(--accent-gold); }
  .side-brand .brand-name { font-size: 13px; }
</style>
</head>
<body>
<main class="sheet">

  <section class="label label--chocolate">
    <div class="band band--top"><span class="flavor">Chocolate</span></div>
    <div class="front">
      <div class="brand"><span class="brand-dot"></span><span class="brand-name">ORVANTA</span></div>
      <div class="brand-tagline">NUTRITION RESULTS</div>
      <h1 class="product-name">MERO LUX</h1>
      <p class="ingredients">WHEY PROTEIN ISOLATE • EGG PROTEIN ISOLATE • CALCIUM CASEINATE</p>
    </div>
    <div class="badges"><span class="badge"></span><span class="badge"></span><span class="badge"></span></div>
    <div class="side">
      <h2 class="side-title">MERO LUX</h2>
      <p class="side-copy">Premium blend of fast and slow proteins to support recovery and lean muscle growth after training.</p>
      <p class="side-copy">Mix one scoop with 300 ml water or milk.</p>
      <div class="side-brand"><span class="brand-dot"></span><span class="brand-name">ORVANTA</span></div>
    </div>
    <div class="band band--bottom"><span class="net-weight">Food supplement. net wt. 2kg</span></div>
  </section>

  <section class="label label--banana">
    <div class="band band--top"><span class="flavor">Banana</span></div>
    <div class="front">
      <div class="brand"><span class="brand-dot"></span><span class="brand-name">ORVANTA</span></div>
      <div class="brand-tagline">NUTRITION RESULTS</div>
      <h1 class="product-name">MERO LUX</h1>
      <p class="ingredients">WHEY PROTEIN ISOLATE • EGG PROTEIN ISOLATE • CALCIUM CASEINATE</p>
    </div>
    <div class="badges"><span class="badge"></span><span class="badge"></span><span class="badge"></span></div>
    <div class="side">
      <h2 class="side-title">MERO LUX</h2>
      <p class="side-copy">Premium blend of fast and slow proteins to support recovery and lean muscle growth after training.</p>
      <p class="side-copy">Mix one scoop with 300 ml water or milk.</p>
      <div class="side-brand"><span class="brand-dot"></span><span class="brand-name">ORVANTA</span></div>
    </div>
    <div class="band band--bottom"><span class="net-weight">Food supplement. net wt. 2kg</span></div>
  </section>

  <section class="label label--strawberry">
    <div class="band band--top"><span class="flavor">Strawberry</span></div>
    <div class="front">
      <div class="brand"><span class="brand-dot"></span><span class="brand-name">ORVANTA</span></div>
      <div class="brand-tagline">NUTRITION RESULTS</div>
      <h1 class="product-name">MERO LUX</h1>
      <p class="ingredients">WHEY PROTEIN ISOLATE • EGG PROTEIN ISOLATE • CALCIUM CASEINATE</p>
    </div>
    <div class="badges"><span class="badge"></span><span class="badge"></span><span class="badge"></span></div>
    <div class="side">
      <h2 class="side-title">MERO LUX</h2>
      <p class="side-copy">Premium blend of fast and slow proteins to support recovery and lean muscle growth after training.</p>
      <p class="side-copy">Mix one scoop with 300 ml water or milk.</p>
      <div class="side-brand"><span class="brand-dot"></span><span class="brand-name">ORVANTA</span></div>
    </div>
    <div class="band band--bottom"><span class="net-weight">Food supplement. net wt. 2kg</span></div>
  </section>

  <section class="label label--vanilla">
    <div class="band band--top"><span class="flavor">Vanilla</span></div>
    <div class="front">
      <div class="brand"><span class="brand-dot"></span><span class="brand-name">ORVANTA</span></div>
      <div class="brand-tagline">NUTRITION RESULTS</div>
      <h1 class="product-name">MERO LUX</h1>
      <p class="ingredients">WHEY PROTEIN ISOLATE • EGG PROTEIN ISOLATE • CALCIUM CASEINATE</p>
    </div>
    <div class="badges"><span class="badge"></span><span class="badge"></span><span class="badge"></span></div>
    <div class="side">
      <h2 class="side-title">MERO LUX</h2>
      <p class="side-copy">Premium blend of fast and slow proteins to support recovery and lean muscle growth after training.</p>
      <p class="side-copy">Mix one scoop with 300 ml water or milk.</p>
      <div class="side-brand"><span class="brand-dot"></span><span class="brand-name">ORVANTA</span></div>
    </div>
    <div class="band band--bottom"><span class="net-weight">Food supplement. net wt. 2kg</span></div>
  </section>

</main>
</body>
</html>
```